Masonry and Landscaping Construction company business card

Looking for a business card design for a construction company named Ferrano Construction. It is an italian-american family business that specializes in custom stone work, patios, walkways, driveways, steps, outdoor kitchens, concrete, waterproofing, power wash, landscaping and more. Our colors are mostly red and white with some black. We're looking for a bold design. we also like to incorporate a picture of my family's hometown somewhere in it.
Target Market(s)
Luxury home owners
Industry/Entity Type
Construction
Contact Information for Business Card
Details includes should be bullet points mentioning the services provided. Custom Stone Work, Outdoor Kitchens, Fire Pits, Patios, Walkways, Steps, Concrete, Waterproofing, powerwash and landscaping
Requirements
Must have
- Would like a spot on the card for co-owners names, numbers and email to be listed also looking to add the QR code for an instagram page
Nice to have
- would like something bold, based around the colors red and white with black outlines or details

```html
<!DOCTYPE html>
<html lang="en">
<head>
<meta charset="utf-8">
<title>Ferrano Construction – Business Card</title>
<link href="https://fonts.googleapis.com/css2?family=Ubuntu:wght@400;500;700&display=swap" rel="stylesheet">
<style>
  :root {
    --brand-red: #d71f27;
    --ink: #1e1e1e;
    --paper: #ffffff;
    --backdrop: #3a3a3c;
    --divider: #111111;
  }
  * { margin: 0; padding: 0; box-sizing: border-box; }
  html, body { width: 1200px; height: 1059px; overflow: hidden; }
  body {
    background: var(--backdrop);
    font-family: "Ubuntu", sans-serif;
    position: relative;
  }
  .card {
    position: absolute;
    border-radius: 22px;
    overflow: hidden;
    box-shadow: 0 8px 18px rgba(0,0,0,0.55);
  }
  .card-front {
    left: 256px; top: 100px; width: 688px; height: 391px;
    background: var(--paper);
  }
  .card-back {
    left: 253px; top: 537px; width: 694px; height: 394px;
    background: var(--brand-red);
  }
  .brand-mark {
    position: absolute;
    display: flex; align-items: center; gap: 10px;
    font-weight: 700;
    letter-spacing: 1px;
    line-height: 1.05;
  }
  .brand-mark .mark-square {
    width: 22px; height: 22px; flex: none;
  }
  .card-front .brand-mark {
    left: 40px; top: 170px; width: 230px;
    transform: translateY(-50%);
    color: var(--ink); font-size: 26px;
  }
  .card-front .brand-mark .mark-square { background: var(--brand-red); }
  .card-back .brand-mark {
    left: 50%; top: 148px;
    transform: translate(-50%, -50%);
    color: var(--paper); font-size: 36px;
    text-align: left;
  }
  .card-back .brand-mark .mark-square { background: var(--paper); width: 30px; height: 30px; }
  .owner-name {
    position: absolute; left: 40px; top: 229px;
    color: var(--brand-red); font-size: 27px; font-weight: 500; letter-spacing: 0.5px;
  }
  .owner-role {
    position: absolute; left: 40px; top: 262px;
    color: var(--ink); font-size: 15.5px; letter-spacing: 0.4px;
  }
  .accent-rule {
    position: absolute; left: 40px; top: 291px;
    width: 20px; height: 2px; background: var(--brand-red);
  }
  .contact-list { position: absolute; left: 40px; top: 308px; list-style: none; }
  .contact-list li {
    display: flex; align-items: center; gap: 12px;
    font-size: 16.5px; color: var(--ink); height: 26px;
  }
  .contact-list svg { width: 14px; height: 14px; flex: none; }
  .card-divider {
    position: absolute; left: 344px; top: 0; width: 7px; height: 100%;
    background: var(--divider);
  }
  .hometown-photo {
    position: absolute; left: 351px; top: 0; right: 0; bottom: 0;
    background:
      linear-gradient(180deg, #b9c2cb 0%, #cfd4d8 18%, #6f8e6a 30%, #4f7a45 48%, #b08a6c 62%, #9c7a62 78%, #5c7f3e 100%);
  }
  .services {
    position: absolute; left: 0; right: 0; top: 320px;
    text-align: center; color: var(--paper);
    font-size: 16px; line-height: 22px; letter-spacing: 0.2px;
  }
</style>
</head>
<body>
  <section class="card card-front">
    <div class="brand-mark"><span class="mark-square"></span><span>FERRANO CONSTRUCTION</span></div>
    <h1 class="owner-name">DARIO VITALE</h1>
    <p class="owner-role">CO-OWNERS</p>
    <div class="accent-rule"></div>
    <ul class="contact-list">
      <li>
        <svg viewBox="0 0 24 24" fill="none" stroke="#d71f27" stroke-width="2.4" stroke-linecap="round" stroke-linejoin="round"><path d="M5 3h4l2 5-2.5 1.5a11 11 0 0 0 6 6L16 13l5 2v4a2 2 0 0 1-2 2A17 17 0 0 1 3 5a2 2 0 0 1 2-2z"/></svg>
        (516)555-0142
      </li>
      <li>
        <svg viewBox="0 0 24 24"><rect x="2" y="4" width="20" height="16" rx="1.5" fill="#d71f27"/><path d="M3 6l9 7 9-7" fill="none" stroke="#fff" stroke-width="2.2"/></svg>
        info@ferranostone.com
      </li>
    </ul>
    <div class="card-divider"></div>
    <div class="hometown-photo" role="img" aria-label="Photograph of the family's Italian hometown: a hillside village with a stone church and bell tower below green mountains"></div>
  </section>

  <section class="card card-back">
    <div class="brand-mark"><span class="mark-square"></span><span>FERRANO<br>CONSTRUCTION</span></div>
    <p class="services">CUSTOM STONE WORK, OUTDOOR KITCHENS, FIRE PITS, PATIOS, WALKWAYS,<br>STEPS, CONCRETE, WATERPROOFING, POWERWASH AND LANDSCAPING</p>
  </section>
</body>
</html>
```